Letterhead and Business card for Construction company

We need a letterhead and business card with our new company logo. We are based in NY. We develop and build properties.

The design should incorporate some unique feature from the logo (shape, font...). it should look like an extension from it.

Design should be clean and elegant, professional, not too busy.

The letterhead should include:
Logo (attached)
Address
Phone
Email

Please find the attached logo images and AI file.

Target Market(s)

Construction industry professionals

Industry/Entity Type

Construction, Development

Font styles to use
Sans Serif

Colors

Designer to choose colors to be used in the design.

Requirements
Must have
• Design should incorporate logo elements, additional assets are welcome. I'd like to see some other shapes / images invorporated too.

```html
<!DOCTYPE html>
<html lang="en">
<head>
<meta charset="utf-8">
<title>Halden Build Co. — Stationery</title>
<link href="https://fonts.googleapis.com/css2?family=Raleway:wght@400;500;700;800&family=Arimo:wght@400&display=swap" rel="stylesheet">
<style>
  :root {
    --ink: #1d1c1d;
    --charcoal: #232124;
    --paper: #f6f6f5;
    --orange: #f07a1f;
    --muted: #3a3a3a;
    --emboss: #0c0c0c;
    --backdrop: #d9d6d1;
  }
  * { box-sizing: border-box; margin: 0; padding: 0; }
  html, body { width: 1200px; height: 960px; overflow: hidden; }
  body {
    background: var(--backdrop);
    font-family: "Raleway", sans-serif;
    color: var(--ink);
    position: relative;
  }

  /* ---------- Brand wordmark ---------- */
  .wordmark {
    display: flex; align-items: center; gap: 8px;
    font-family: "Raleway", sans-serif; font-weight: 800;
    letter-spacing: 0.5px; white-space: nowrap;
  }
  .wordmark .mark-square { width: 14px; height: 14px; background: var(--orange); flex: none; }

  /* ---------- Icons ---------- */
  .contact-line { display: flex; align-items: center; gap: 6px; white-space: nowrap; }
  .icon { width: 9px; height: 9px; flex: none; }
  .icon-fill { fill: var(--orange); }
  .icon-stroke { fill: none; stroke: var(--orange); stroke-width: 1.3; }

  /* ---------- Letterhead ---------- */
  .letterhead {
    position: absolute; left: 506px; top: 126px;
    width: 510px; height: 720px;
    background: var(--paper);
    box-shadow: 0 2px 10px rgba(0,0,0,.18);
  }
  .letterhead .wordmark {
    position: absolute; left: 0; right: 0; top: 92px;
    justify-content: center; font-size: 24px; color: var(--ink);
  }
  .letter-body {
    position: absolute; left: 109px; width: 358px; top: 162px;
    font-family: "Arimo", sans-serif; font-size: 9.6px; line-height: 11.4px;
    color: #111; text-align: justify;
  }
  .letter-body p { margin-bottom: 18px; }
  .letter-body p.gap { margin-bottom: 24px; }
  .letter-footer {
    position: absolute; left: 0; right: 0; bottom: 0; height: 35px;
    background: var(--charcoal); color: #fff;
    display: flex; align-items: center; justify-content: flex-end;
    font-size: 10px; line-height: 13px; padding-right: 14px;
  }
  .letter-footer .col { padding: 0 12px; border-left: 1px solid var(--orange); white-space: nowrap; }
  .letter-footer .col:first-child { border-left: none; }

  /* ---------- Business cards ---------- */
  .card {
    position: absolute; left: 136px; width: 334px; height: 198px;
    border-radius: 10px; overflow: hidden;
    box-shadow: 0 3px 10px rgba(0,0,0,.25);
  }
  .card-front { top: 262px; background: var(--charcoal); }
  .card-front .wordmark {
    position: absolute; left: 0; right: 0; top: 84px;
    justify-content: center; font-size: 24px; color: var(--emboss);
  }
  .card-front .wordmark .mark-square { background: var(--emboss); }

  .card-back { top: 502px; background: var(--paper); }
  .card-back .wordmark {
    position: absolute; right: 22px; top: 52px;
    font-size: 15px; color: var(--ink); gap: 6px;
  }
  .card-back .wordmark .mark-square { width: 10px; height: 10px; }
  .holder-name {
    position: absolute; left: 17px; top: 100px;
    font-weight: 700; font-size: 16px; color: #222;
  }
  .holder-title {
    position: absolute; left: 17px; top: 121px;
    font-size: 9.5px; color: var(--muted);
  }
  .card-rule {
    position: absolute; left: 17px; right: 22px; top: 138px;
    border-top: 1px solid #333;
  }
  .card-contacts {
    position: absolute; left: 17px; top: 147px;
    font-size: 9.2px; line-height: 13.8px; color: var(--muted);
  }
  .card-address {
    position: absolute; right: 17px; top: 162px;
    font-size: 9.5px; line-height: 13.4px; color: var(--muted); text-align: left;
  }
</style>
</head>
<body>

  <section class="card card-front" aria-label="Business card front">
    <div class="wordmark"><span class="mark-square"></span>HALDEN BUILD CO.</div>
  </section>

  <section class="card card-back" aria-label="Business card back">
    <div class="wordmark"><span class="mark-square"></span>HALDEN BUILD CO.</div>
    <div class="holder-name">MARCUS REED</div>
    <div class="holder-title">Managing Director</div>
    <div class="card-rule"></div>
    <div class="card-contacts">
      <div class="contact-line">
        <svg class="icon icon-fill" viewBox="0 0 10 10"><path d="M2 0.5 L4 2.6 3 3.8 Q4.2 6 6.2 7 L7.4 6 9.5 8 8.2 9.5 Q4.5 9.5 0.5 1.8Z"/></svg>212-555 0148</div>
      <div class="contact-line">
        <svg class="icon icon-stroke" viewBox="0 0 10 10"><rect x="0.7" y="2" width="8.6" height="6"/><path d="M0.7 2 L5 5.5 L9.3 2"/></svg>hello@haldenbuild.com</div>
      <div class="contact-line">
        <svg class="icon icon-stroke" viewBox="0 0 10 10"><circle cx="5" cy="5" r="4.2"/><path d="M0.8 5h8.4M5 0.8q-2.6 4.2 0 8.4M5 0.8q2.6 4.2 0 8.4"/></svg>www.haldenbuild.com</div>
    </div>
    <div class="card-address">88 Harbor Street<br>New York, NY 10013</div>
  </section>

  <section class="letterhead" aria-label="Letterhead">
    <div class="wordmark"><span class="mark-square"></span>HALDEN BUILD CO.</div>

    <div class="letter-body">
      <p>Lorem ipsum dolor sit amet, consectetur adipiscing elit. Donec fringilla neque euismod volutpat cursus. Vestibulum ac pretium orci, consequat elementum velit. Etiam bibendum purus ac augue finibus volutpat. Vestibulum justo nisl.</p>
      <p class="gap">Lorem ipsum dolor sit amet, consectetur adipiscing elit. Donec fringilla neque euismod volutpat cursus. Vestibulum ac pretium orci, consequat elementum velit. Etiam bibendum purus ac augue finibus volutpat. Vestibulum justo nisl, gravida aliquet sollicitudin ut, finibus vitae mi. Praesent aliquet scelerisque blandit. Sed id varius lacus, id tristique sem. Fusce et lobortis leo. Aliquam mollis pellentesque magna, condimentum ullamcorper ex ullamcorper non. Morbi ultricies nunc eu tellus dignissim, eget venenatis dolor ullamcorper. Etiam dolor eros, iaculis at ultricies nec, volutpat nec orci. Vivamus tincidunt rutrum sapien, ac porttitor mauris tristique nec.</p>
      <p>Lorem ipsum dolor sit amet, consectetur adipiscing elit. Donec fringilla neque euismod volutpat cursus. Vestibulum ac pretium orci, consequat elementum velit. Etiam bibendum purus ac augue finibus volutpat. Vestibulum justo nisl, gravida aliquet sollicitudin ut, finibus vitae mi. Praesent aliquet scelerisque blandit. Sed id varius lacus, id tristique sem. Fusce et lobortis leo. Aliquam mollis pellentesque magna, condimentum ullamcorper ex ullamcorper non. Morbi ultricies nunc eu tellus dignissim, eget venenatis dolor ullamcorper. Etiam dolor eros, iaculis at ultricies nec, volutpat nec orci. Vivamus tincidunt rutrum sapien, ac porttitor mauris tristique nec.</p>
      <p>Lorem ipsum dolor sit amet, consectetur adipiscing elit. Donec fringilla neque euismod volutpat cursus. Vestibulum ac pretium orci, consequat elementum velit. Etiam bibendum purus ac augue finibus volutpat. Vestibulum justo nisl.</p>
      <p>Lorem ipsum dolor sit amet, consectetur adipiscing elit. Donec fringilla neque euismod volutpat cursus. Vestibulum ac pretium orci, consequat elementum velit. Etiam bibendum purus ac augue finibus volutpat. Vestibulum justo nisl, gravida aliquet sollicitudin ut, finibus vitae mi. Praesent aliquet scelerisque blandit. Sed id varius lacus, id tristique sem. Fusce et lobortis leo. Aliquam mollis pellentesque magna, condimentum ullamcorper ex ullamcorper non. Morbi ultricies nunc eu tellus dignissim, eget venenatis dolor ullamcorper. Etiam dolor eros, iaculis at ultricies nec, volutpat nec orci. Vivamus tincidunt rutrum sapien, ac porttitor mauris tristique nec.</p>
    </div>

    <footer class="letter-footer">
      <div class="col">
        <div class="contact-line">
          <svg class="icon icon-fill" viewBox="0 0 10 10"><path d="M2 0.5 L4 2.6 3 3.8 Q4.2 6 6.2 7 L7.4 6 9.5 8 8.2 9.5 Q4.5 9.5 0.5 1.8Z"/></svg>212-555 0148</div>
        <div class="contact-line">
          <svg class="icon icon-stroke" viewBox="0 0 10 10"><rect x="0.7" y="2" width="8.6" height="6"/><path d="M0.7 2 L5 5.5 L9.3 2"/></svg>hello@haldenbuild.com</div>
      </div>
      <div class="col">88 Harbor Street<br>New York, NY 10013</div>
      <div class="col">www.haldenbuild.com</div>
    </footer>
  </section>

</body>
</html>
```